Label for Skincare Brand

"Fernleigh Vale Organics" - organic skincare brand
I need a label designed for my organic skincare brand. I have attached pics of brands I like, to give you an idea of style. I would like something minimal although some colour might work. Colours I like are pale blush pink and aqua. I would like a clean, minimalistic modern yet elegant label. Please look at the samples because they demonstrate the style I look for in a label. It is okay to add a graphical element into the design as long as it enhances or add value to the design.
We do not have a logo yet, so I'd appreciate if you could create a simple type logo for Fernleigh Vale Organics similar to the examples attached.
Please can you do two different sizes: one cream jar and one serum bottle. Both will contain the same information.
___________________________________________________
1. Cream Jar (label size 42 x 190 mm) (clear glass with aluminium lid)
2. Serum Bottle (label size 50 x 110 mm) (clear glass with black pump)
FRONT SIDE:
Fernleigh Vale Organics
Nine Moons
Ultimate Anti-Aging Cream
For Dry & Mature Skin
Organic & Palm Oil-Free
100 ml.
BACK SIDE:
Nine Moons Ultimate Anti-Aging Cream
An effective Day Cream that harnesses the best of science to target the signs of aging. The main active ingredient is R58, a patented noncomedogenic lipid complex, carefully engineered from botanically-sourced lipids. It is composed of a variety of lipid types which are carefully combined in the same ratio as those found on healthy young skin of an average 22 year old.
Directions:
Apply to clean skin morning and night.
Ingredients:
Aloe Vera Leaf Juice, Cocos Nucifera Oil, Butyrospermum Parkii Butter, Jojoba Oil/Macadamia Seed Oil Esters (and) Squalene (and) Phytosteryl Macadamiate (and) Phytosterols, Potassium Olivoyl Hydrolyzed Oat Protein (and) Cetearyl Alcohol (and) Glyceryl Oleate (and) Glyceryl Stearat, Benzyl Alcohol, Dehydroacetic Acid.
Fernleigh Vale Organics
6/3 Kelmora Street North, Ashgrove Hill, NSW 2190
www.fernleighvaleorganics.com.au
Any questions, please just ask away. Thank you.

```html
<!DOCTYPE html>
<html lang="en">
<head>
<meta charset="utf-8">
<title>Fernleigh Vale Organics — Nine Moons Labels</title>
<link href="https://fonts.googleapis.com/css2?family=Roboto+Mono:wght@400;500;700&family=Montserrat:wght@300&display=swap" rel="stylesheet">
<style>
  :root {
    --canvas: #eef3f4;
    --label: #cfe8ee;
    --ink: #1f2326;
    --aqua: #63c2d0;
  }
  * { margin: 0; padding: 0; box-sizing: border-box; }
  html, body { width: 1200px; height: 881px; overflow: hidden; background: var(--canvas); }
  body { position: relative; font-family: "Roboto Mono", monospace; color: var(--ink); }

  .label { position: absolute; background: var(--label); }
  .jar-front { left: 60px; top: 50px; width: 1080px; height: 240px; }
  .jar-back  { left: 60px; top: 320px; width: 1080px; height: 240px; }
  .serum     { left: 60px; top: 590px; width: 528px; height: 240px; }

  /* Type logo: one font, one weight, one colour */
  .wordmark {
    font-family: "Roboto Mono", monospace;
    font-weight: 500;
    text-transform: uppercase;
    letter-spacing: 0.08em;
    white-space: nowrap;
    color: var(--ink);
    line-height: 1.2;
  }

  .variant { text-transform: uppercase; letter-spacing: 0.04em; white-space: nowrap; }
  .volume { letter-spacing: 0.02em; white-space: nowrap; }
  .product-name {
    font-family: "Montserrat", sans-serif; font-weight: 300;
    color: var(--aqua); letter-spacing: 0.05em; text-transform: uppercase;
    white-space: nowrap;
  }
  .claims { text-transform: uppercase; line-height: 1.35; letter-spacing: 0.01em; white-space: nowrap; }

  /* Jar front */
  .jar-front .front-block {
    position: absolute; left: 50%; top: 50%; transform: translate(-50%, -50%);
    display: flex; gap: 64px; align-items: flex-end;
  }
  .jar-front .wordmark { font-size: 20px; }
  .jar-front .variant { font-size: 20px; margin-top: 28px; }
  .jar-front .volume { font-size: 20px; margin-top: 4px; }
  .jar-front .details { text-align: right; }
  .jar-front .product-name { font-size: 40px; line-height: 1; margin-bottom: 6px; }
  .jar-front .claims { font-size: 16px; }

  /* Jar back */
  .jar-back .back-copy {
    position: absolute; left: 160px; right: 160px; top: 22px;
    font-size: 10.5px; line-height: 1.38;
  }
  .back-title {
    text-align: center; font-weight: 700; font-size: 14px;
    text-transform: uppercase; letter-spacing: 0.03em; margin-bottom: 8px;
  }
  .back-copy p { margin-bottom: 6px; }
  .back-copy strong { font-weight: 700; }
  .maker {
    position: absolute; right: 160px; bottom: 16px;
    font-size: 10px; line-height: 1.35; text-align: right;
  }

  /* Serum */
  .serum .front-block {
    position: absolute; left: 50%; top: 50%; transform: translate(-50%, -50%);
    width: 290px;
  }
  .serum .wordmark { font-size: 14.5px; }
  .serum .variant { font-size: 15px; margin-top: 22px; }
  .serum .volume { font-size: 18px; margin-top: 2px; }
  .serum .product-name { font-size: 24px; text-align: right; margin-top: 6px; line-height: 1.1; }
  .serum .claims { font-size: 12.5px; text-align: right; margin-top: 4px; }
</style>
</head>
<body>

<section class="label jar-front" aria-label="Cream jar front label">
  <div class="front-block">
    <div class="brand">
      <div class="wordmark">Fernleigh Vale Organics</div>
      <div class="variant">Nine Moons</div>
      <div class="volume">100 ml.</div>
    </div>
    <div class="details">
      <div class="product-name">Ultimate</div>
      <div class="claims">Anti-Aging Cream<br>For Dry &amp; Mature Skin<br>Organic &amp; Palm Oil-Free</div>
    </div>
  </div>
</section>

<section class="label jar-back" aria-label="Cream jar back label">
  <div class="back-copy">
    <h2 class="back-title">Nine Moons Ultimate Anti-Aging Cream</h2>
    <p>An effective Day Cream that harnesses the best of science to target the signs of aging. The main active ingredient is R58, a patented noncomedogenic lipid complex, carefully engineered from botanically-sourced lipids. It is composed of a variety of lipid types which are carefully combined in the same ratio as those found on healthy young skin of an average 22 year old.</p>
    <p><strong>Directions:</strong> Apply to clean skin morning and night.</p>
    <p><strong>Ingredients:</strong> Aloe Vera Leaf Juice, Cocos Nucifera Oil, Butyrospermum Parkii Butter, Jojoba Oil/Macadamia Seed Oil Esters (and) Squalene (and) Phytosteryl Macadamiate (and) Phytosterols, Potassium Olivoyl Hydrolyzed Oat Protein (and) Cetearyl Alcohol (and) Glyceryl Oleate (and) Glyceryl Stearat, Benzyl Alcohol, Dehydroacetic Acid.</p>
  </div>
  <div class="maker">
    Fernleigh Vale Organics<br>
    6/3 Kelmora Street North, Ashgrove Hill, NSW 2190<br>
    www.fernleighvaleorganics.com.au
  </div>
</section>

<section class="label serum" aria-label="Serum bottle front label">
  <div class="front-block">
    <div class="wordmark">Fernleigh Vale Organics</div>
    <div class="variant">Nine Moons</div>
    <div class="volume">100 ml.</div>
    <div class="product-name">Ultimate</div>
    <div class="claims">Anti-Aging Cream<br>For Dry &amp; Mature Skin<br>Organic &amp; Palm Oil-Free</div>
  </div>
</section>

</body>
</html>
```